Website design for Cambridge based systematic hedge fund

We have run previous craftmosaic competitions to design our company logo, business cards and the styling of our presentation deck (see attached files).
As the final step we are looking to get a website designed that is thematically consistent with these existing elements of our branding.
You can find some of our competitors websites below:
https://www.quelmarsh.example/
https://www.fenloor.example/
https://www.pyvart.example/
https://www.dulvet.example/
https://www.orbelmfunds.example/
https://www.valtrigo.example/
https://www.meskilfunds.example/home
We would like to have a website that works well on both mobile devices and desktops. Either just as one page that can be scrolled down, with links at the top that skips to certain sections, or a few separate pages that can be navigated by a top menu.
It should look professional, we are not after lots of animations or unnecessary transitions, and in particular the website must be smooth to navigate. We would like to avoid having peoples of people, we are happy to make use of elements from the presentation (for example the style of the cover slide, or the section slides with the faded bridge in the background), or 'financial' style images.
We would like to have the following sections for now. For some of these some example text has been provided, final text may change but it will be of similar length. For the other sections we are happy to just have template text for now. At the moment we are mainly interested to see styles/layouts as words can be added easily afterwards:
1) We will need a disclaimer pop up the first time someone visits the site (see for example the meskilfunds example).
2) Top page - company name, then in larger text "Bringing AI and Statistical Inference to Financial Markets", and somewhere in smaller text "Harlow Vectors is a quantitative asset manager with the singular focus of delivering algorithmic strategies that work"
3) "About us" section: will describe us as a company, details our approach, company values, and explains the company logo.
Example text:
"We deliver consistent alpha across liquid markets through the application of proprietary IP in Bayesian inference, machine learning and artificial intelligence. We are a multi-disciplinary team founded by experienced finance professionals from premier institutions, leading academics from the Thornbury Stellar Unit at Ashmere College and world-class software engineers.
Our logo portrays a sillhoute of the lattice walkway at Ashmere College. Our unique scientific approach allows us to bridge cutting-edge mathematical research and computing expertise with financial knowledge to bring algorithmns that work to liquid markets"
4) Hiring section, detailing our culture, what we are looking for.
Example text:
"We are always looking for exceptional talent to join our entrepreneurial team. We are looking for individuals who are creative thinkers, can demonstrate analytical rigour and are passionate about the intersection of science, finance and technology.
We prioritise having a company culture that promotes sharing ideas in a safe, collaborative research environment. We make sure that every member of the team has the oppertunity to explore their own ideas through weekly 'innovation time', and ensure that everyone gets the support they need to continue to grow as individuals within the company."
5) A section for news/press releases
6) Contact us area at the bottom with office location and email. We will need to list 3 addresses for our Cambridge, London and Singapore offices, along with a couple of contact emails or phone numbers
7) A client login button at the top that will take them to a different website (unrelated to this one).

```html
<!DOCTYPE html>
<html lang="en">
<head>
<meta charset="utf-8">
<title>Harlow Vectors</title>
<link href="https://fonts.googleapis.com/css2?family=Open+Sans:wght@400;600;700&family=Lato:wght@400;700&family=Roboto:wght@400;500&display=swap" rel="stylesheet">
<style>
:root{
  --navy:#14305e;
  --blue:#4a7fc1;
  --blue-soft:rgba(74,127,193,.93);
  --footer:#10305c;
  --text:#555a60;
  --white:#ffffff;
  --cream:#f5f2ec;
}
*{margin:0;padding:0;box-sizing:border-box}
html,body{width:1200px;height:2881px;overflow:hidden}
body{position:relative;font-family:'Lato',sans-serif;color:var(--text);background:var(--white)}
.abs{position:absolute}
a{color:inherit;text-decoration:none}
h1,h2,h3,h4{font-weight:inherit}

/* header */
.site-header{left:0;top:0;width:1200px;height:100px;background:var(--white)}
.brand{left:112px;top:37px;display:flex;align-items:center;gap:8px;font-family:'Open Sans',sans-serif;font-weight:700;font-size:18px;color:var(--navy);white-space:nowrap}
.brand-mark{width:14px;height:14px;background:var(--navy)}
.main-nav{left:316px;top:41px;display:flex;gap:35px;font-family:'Open Sans',sans-serif;font-weight:600;font-size:14px;color:#444}
.main-nav .current{color:var(--navy);border-bottom:2px solid var(--navy);padding-bottom:6px}
.client-login{left:963px;top:29px;width:126px;height:41px;border:2px solid var(--navy);color:var(--navy);font-family:'Open Sans',sans-serif;font-weight:700;font-size:14px;display:flex;align-items:center;justify-content:center}

/* hero */
.hero{left:0;top:100px;width:1200px;height:642px;
  background:
    radial-gradient(ellipse 520px 300px at 640px 240px,rgba(170,170,175,.55),transparent 70%),
    radial-gradient(ellipse 600px 420px at 120px 560px,rgba(20,60,80,.55),transparent 70%),
    linear-gradient(172deg,#767c80 0%,#5a6c74 25%,#3a5d6e 50%,#27506c 75%,#1a3d60 100%)}
.hero-title{left:0;top:293px;width:1200px;text-align:center;font-family:'Open Sans',sans-serif;font-weight:700;font-size:56px;line-height:72px;color:var(--white);letter-spacing:1px}
.hero-sub{left:0;top:362px;width:1200px;text-align:center;font-family:'Open Sans',sans-serif;font-weight:400;font-size:20px;color:var(--white);letter-spacing:.8px}
.btn{display:flex;align-items:center;justify-content:center;font-family:'Open Sans',sans-serif;font-weight:700;color:var(--white);background:var(--blue)}
.btn-outline{background:transparent;border:2px solid var(--white)}
.hero-btn{left:530px;top:412px;width:140px;height:48px;font-size:16px}
.slider-dots{left:570px;top:696px;display:flex;gap:9px}
.slider-dots span{width:8px;height:8px;border-radius:50%;background:var(--white)}
.slider-dots span.on{background:transparent;border:1.5px solid var(--white)}

/* about */
.about-title{left:112px;top:800px;font-family:'Open Sans',sans-serif;font-weight:700;font-size:36px;line-height:43px;color:var(--navy)}
.about-copy{left:112px;top:894px;width:485px;font-size:14px;line-height:23px}
.about-copy p+p{margin-top:12px}
.about-btn{left:112px;top:1122px;width:124px;height:45px;font-size:14px}
.about-photo{left:654px;top:808px;width:434px;height:368px;border:4px solid var(--blue);
  background:
    radial-gradient(ellipse 70px 200px at 225px 210px,rgba(20,20,22,.95),rgba(20,20,22,.6) 60%,transparent 100%),
    linear-gradient(180deg,transparent 75%,rgba(60,50,40,.7) 100%),
    linear-gradient(90deg,#8b7563 0%,#b59c88 18%,#3a3532 28%,#c9ccce 40%,#d7dadc 60%,#2e2e30 70%,#cfd3d6 82%,#b7bcc1 100%)}

/* approach */
.approach{left:0;top:1242px;width:1200px;height:499px;
  background:
    radial-gradient(ellipse 400px 250px at 1050px 200px,rgba(120,125,130,.35),transparent 70%),
    linear-gradient(160deg,#41474b 0%,#2c3237 50%,#1d2328 100%)}
.approach-title{left:0;top:1298px;width:1200px;text-align:center;font-family:'Open Sans',sans-serif;font-weight:600;font-size:35px;color:var(--white)}
.values-box{left:187px;top:1378px;width:827px;height:305px;background:var(--blue-soft)}
.values-title{left:187px;top:1410px;width:827px;text-align:center;font-family:'Open Sans',sans-serif;font-weight:400;font-size:25px;color:var(--white)}
.values-copy{left:217px;top:1451px;width:767px;text-align:center;font-size:13.4px;line-height:23px;color:var(--white)}
.values-btn{left:538px;top:1590px;width:123px;height:40px;font-size:14px}

/* hiring & culture */
.teasers{left:0;top:1741px;width:1200px;height:458px;background:var(--cream)}
.teaser-title{font-family:'Open Sans',sans-serif;font-weight:700;font-size:24px;color:var(--navy)}
.teaser-rule{width:29px;height:4px;background:var(--blue)}
.teaser-copy{width:160px;font-size:14.5px;line-height:23px;color:#666}
.teaser-btn{width:141px;height:45px;font-size:16px}
.teaser-photo{width:260px;height:279px;border:3px solid var(--blue)}
.photo-markets{background:
  radial-gradient(ellipse 120px 160px at 140px 100px,rgba(220,230,250,.7),transparent 70%),
  linear-gradient(135deg,#24438a 0%,#5d82c6 45%,#8aa7dc 55%,#2b4a8c 80%,#15285c 100%)}
.photo-towers{background:
  linear-gradient(100deg,rgba(30,40,70,.7) 0%,transparent 25%,transparent 75%,rgba(30,40,70,.7) 100%),
  linear-gradient(180deg,#3e6fbf 0%,#5b93dc 40%,#7a8ea8 65%,#9a7a52 82%,#3b3d48 100%)}

/* looking for */
.looking{left:0;top:2199px;width:1200px;height:349px;
  background:
    radial-gradient(ellipse 500px 180px at 900px 300px,rgba(40,70,120,.35),transparent 70%),
    linear-gradient(180deg,#6189bf 0%,#5079b2 55%,#4168a2 100%)}
.looking-title{left:0;top:2260px;width:1200px;text-align:center;font-family:'Open Sans',sans-serif;font-weight:700;font-size:36px;color:var(--white)}
.looking-copy{left:205px;top:2319px;width:790px;text-align:center;font-size:16.5px;line-height:23px;color:var(--white)}
.looking-btn{left:523px;top:2418px;width:155px;height:49px;font-size:16px}

/* footer */
.site-footer{left:0;top:2548px;width:1200px;height:333px;background:var(--footer);color:var(--white)}
.footer-head{top:2596px;font-family:'Roboto',sans-serif;font-weight:500;font-size:18px;color:var(--white)}
.footer-links{top:2642px;list-style:none;font-family:'Roboto',sans-serif;font-size:13px;line-height:26.7px;color:var(--white)}
.office{left:620px;top:2645px;font-family:'Roboto',sans-serif;font-size:13px;color:var(--white)}
.office-row{display:flex;gap:7px;align-items:flex-start;line-height:20px}
.office-row svg{margin-top:4px;flex:none}
.social{left:963px;top:2640px;display:flex;gap:5px}
.social span{width:38px;height:38px;border-radius:50%;background:var(--blue);border:2px solid rgba(255,255,255,.25)}
.footer-rule{left:112px;top:2801px;width:976px;height:1px;background:rgba(255,255,255,.15)}
.copyright{left:0;top:2832px;width:1200px;text-align:center;font-family:'Roboto',sans-serif;font-size:12.5px;color:var(--white)}
</style>
</head>
<body>

<header class="abs site-header">
  <a class="abs brand" href="#"><span class="brand-mark"></span>HARLOW VECTORS</a>
  <nav class="abs main-nav">
    <a class="current" href="#">HOME</a>
    <a href="#">ABOUT US</a>
    <a href="#">OUR APPROACH</a>
    <a href="#">HIRING</a>
    <a href="#">OUR CULTURE</a>
    <a href="#">CONTACT US</a>
  </nav>
  <a class="abs client-login" href="#">CLIENT LOGIN</a>
</header>

<section class="abs hero" role="img" aria-label="Upward view of a glass and steel office building"></section>
<h1 class="abs hero-title">HARLOW VECTORS</h1>
<p class="abs hero-sub">We are a Cambridge based systematic hedge fund</p>
<a class="abs btn hero-btn" href="#">LEARN MORE</a>
<div class="abs slider-dots"><span class="on"></span><span></span><span></span><span></span></div>

<h2 class="abs about-title">ABOUT HARLOW<br>VECTORS</h2>
<div class="abs about-copy">
  <p>Lorem ipsum dolor sit amet, consectetur adipiscing elit, sed do eiusmod tempor incididunt ut labore et dolore magna aliqua. Ut enim ad minim veniam, quis nostrud exercitation ullamco laboris nisi ut aliquip ex ea commodo consequat. Duis aute irure dolor in reprehenderit in voluptate velit esse cillum dolore eu fugiat nulla pariatur.</p>
  <p>Sed ut perspiciatis unde omnis iste natus error sit voluptatem accusantium doloremque laudantium, totam rem aperiam, eaque ipsa quae ab illo inventore veritatis et quasi architecto beatae vitae dicta sunt explicabo</p>
</div>
<a class="abs btn about-btn" href="#">LEARN MORE</a>
<div class="abs about-photo" role="img" aria-label="Silhouette of a businessman at an office window overlooking city towers"></div>

<section class="abs approach" role="img" aria-label="Dark financial chart backdrop with candlesticks and a bridge"></section>
<h2 class="abs approach-title">OUR APPROACH</h2>
<div class="abs values-box"></div>
<h3 class="abs values-title">COMPANY VALUES</h3>
<p class="abs values-copy">But I must explain to you how all this mistaken idea of denouncing pleasure and praising pain was born and I will give you a complete account of the system, and expound the actual teachings of the great explorer of the truth, the master-builder of human happiness. No one rejects, dislikes, or avoids pleasure itself, because it is pleasure, but because those who do not know how to pursue pleasure rationally encounter consequences that are extremely painful. Nor again is there anyone who loves or pursues or desires to obtain pain of itself, because it is pain, but because occasionally circumstances.</p>
<a class="abs btn btn-outline values-btn" href="#">LEARN MORE</a>

<section class="abs teasers"></section>
<h3 class="abs teaser-title" style="left:111px;top:1818px">HIRING</h3>
<div class="abs teaser-rule" style="left:112px;top:1866px"></div>
<p class="abs teaser-copy" style="left:112px;top:1897px">Excepteur sint occaecat cupidatat non proident, sunt in culpa qui officia deserunt mollit anim id est laborum</p>
<a class="abs btn teaser-btn" style="left:112px;top:2049px" href="#">LEARN MORE</a>
<div class="abs teaser-photo photo-markets" style="left:309px;top:1818px" role="img" aria-label="Hand reaching toward glowing blue stock market figures"></div>

<h3 class="abs teaser-title" style="left:630px;top:1818px">OUR CULTURE</h3>
<div class="abs teaser-rule" style="left:631px;top:1866px"></div>
<p class="abs teaser-copy" style="left:631px;top:1897px">Excepteur sint occaecat cupidatat non proident, sunt in culpa qui officia deserunt mollit anim id est laborum</p>
<a class="abs btn teaser-btn" style="left:631px;top:2049px" href="#">LEARN MORE</a>
<div class="abs teaser-photo photo-towers" style="left:828px;top:1818px" role="img" aria-label="Skyscrapers seen from street level against a blue sky"></div>

<section class="abs looking" role="img" aria-label="Blue tinted aerial view of a waterfront city skyline"></section>
<h2 class="abs looking-title">WHAT WE ARE LOOKING FOR</h2>
<p class="abs looking-copy">But I must explain to you how all this mistaken idea of denouncing pleasure and praising pain was born and I will give you a complete account of the system, and expound the actual teachings of the great explorer of the truth, the master-builder of human happiness.</p>
<a class="abs btn btn-outline looking-btn" href="#">LEARN MORE</a>

<footer class="abs site-footer"></footer>
<h4 class="abs footer-head" style="left:112px">Links</h4>
<ul class="abs footer-links" style="left:112px">
  <li>Home</li><li>About Us</li><li>Our Approach</li><li>Hiring</li><li>Our Culture</li>
</ul>
<h4 class="abs footer-head" style="left:369px">Resources</h4>
<ul class="abs footer-links" style="left:369px">
  <li>Terms of Use</li><li>Privacy Policy</li><li>Site Map</li><li>Contact Us</li>
</ul>
<h4 class="abs footer-head" style="left:620px">Office Location</h4>
<div class="abs office">
  <div class="office-row">
    <svg width="8" height="11" viewBox="0 0 8 11"><path d="M4 0a4 4 0 0 0-4 4c0 3 4 7 4 7s4-4 4-7a4 4 0 0 0-4-4zm0 5.5A1.5 1.5 0 1 1 4 2.5a1.5 1.5 0 0 1 0 3z" fill="#fff"/></svg>
    <span>Harlowvectors, Street Name,<br>City Address, Country code.</span>
  </div>
  <div class="office-row" style="margin-top:14px">
    <svg width="11" height="11" viewBox="0 0 11 11"><path d="M2.2 0l2 2.6-1.1 1.5a7 7 0 0 0 3.8 3.8l1.5-1.1L11 8.8 9.6 11C4.5 10.6.4 6.5 0 1.4z" fill="#fff"/></svg>
    <span style="font-weight:500">+1 555 010 2040</span>
  </div>
  <div class="office-row" style="margin-top:18px">
    <svg width="12" height="10" viewBox="0 0 12 10"><rect width="12" height="10" rx="1" fill="#fff"/><path d="M0 1l6 4 6-4" stroke="#10305c" stroke-width="1.3" fill="none"/></svg>
    <span style="font-weight:500">info@harlowvectors.example</span>
  </div>
</div>
<h4 class="abs footer-head" style="left:963px">Connect Us</h4>
<div class="abs social" aria-label="Social profiles"><span></span><span></span><span></span></div>
<div class="abs footer-rule"></div>
<p class="abs copyright">Copyrights © 2021 Harlow Vectors.&nbsp; All rights reserved.</p>

</body>
</html>
```